Banner Graphics For Quillo Storefront Page

Hello,
I am looking for a designer to help me with a banner heading that I want to place on my Quillo storefront page. My company sells outdoor kitchen/bbq island accessories. I would like for it to have a background photo with text/logo & graphics overlaid on the image. If possible I would like it to include the 5 small "benefit boxes" that are attached on the file that features graphics for one of the products that I sell . I have also included a color photo of my products in actual use. Feel free to use it but if you have a better idea of a background image feel free to try it, maybe a lifestyle stock photo?? Or maybe something else?? I am open to all ideas and you are the creative ones:) Feel free to be creative. The pixel requirements for final image is 3,000 pixels by 600 pixels. Let me know if you have any questions. THANKS! P.s. I also included some stock photos that I like to give you some ideas.

```html
<!DOCTYPE html>
<html lang="en">
<head>
<meta charset="utf-8">
<title>Crestline Outdoor Kitchens – Quillo Storefront Banner</title>
<link href="https://fonts.googleapis.com/css2?family=Raleway:wght@300;400;700;800&family=Libre+Baskerville&display=swap" rel="stylesheet">
<style>
  :root {
    --page: #ffffff;
    --sage: #9ba99d;
    --sage-light: #a9b6ab;
    --photo-wall: #b7c2bb;
    --photo-steel: #8f9592;
    --photo-floor: #9a9e9a;
    --ink: #2c2c2c;
    --white: #ffffff;
    --badge-border: #2bb3b1;
    --badge-label: #7d7d7d;
    --badge-dark: #2f2f2f;
  }
  * { margin: 0; padding: 0; box-sizing: border-box; }
  html, body { width: 1200px; height: 1200px; overflow: hidden; background: var(--page); }
  .canvas { position: relative; width: 1200px; height: 1200px; }

  .banner {
    position: absolute; left: 0; top: 480px;
    width: 1200px; height: 240px;
    background: var(--sage);
    overflow: hidden;
  }
  .banner-photo {
    position: absolute; left: 328px; top: 0; width: 872px; height: 240px;
    background:
      linear-gradient(180deg, var(--photo-wall) 0%, #c3ccc6 30%, var(--photo-wall) 65%, var(--photo-floor) 100%);
    -webkit-mask-image: linear-gradient(90deg, transparent 0%, #000 10%, #000 85%, transparent 100%);
            mask-image: linear-gradient(90deg, transparent 0%, #000 10%, #000 85%, transparent 100%);
  }

  .brand { position: absolute; left: 42px; top: 14px; width: 150px; text-align: center; }
  .brand-name {
    font-family: "Libre Baskerville", serif; font-size: 27px; color: var(--ink);
    letter-spacing: 0.5px; line-height: 1; margin-top: 14px;
  }
  .brand-tagline {
    font-family: "Libre Baskerville", serif; font-size: 11.5px; color: var(--ink);
    letter-spacing: 1.6px; margin-top: 10px;
  }

  .benefits { position: absolute; left: 18px; top: 106px; display: flex; gap: 9px; }
  .benefit {
    width: 70px; height: 126px; border: 1.5px solid var(--badge-border); border-radius: 7px;
    overflow: hidden; background: var(--white); display: flex; flex-direction: column;
    font-family: "Raleway", sans-serif; text-align: center;
  }
  .benefit-mark { height: 59px; display: flex; align-items: center; justify-content: center; color: var(--ink); }
  .benefit-label {
    height: 20px; background: var(--badge-label); color: var(--white);
    font-weight: 800; font-size: 8.5px; display: flex; align-items: center; justify-content: center; line-height: 1;
  }
  .benefit-text {
    flex: 1; background: var(--badge-dark); color: var(--white);
    font-weight: 700; font-size: 6.3px; line-height: 1.15;
    display: flex; align-items: center; justify-content: center; padding: 0 5px;
  }
  .mark-double { font-weight: 800; font-size: 13px; line-height: 0.9; }
  .mark-double small { display: block; font-size: 5.5px; font-weight: 800; margin-top: 3px; }
  .mark-grade { font-weight: 800; font-size: 5.5px; }
  .mark-grade b { display: block; background: var(--ink); color: var(--white); font-size: 14px; margin: 3px 0; padding: 1px 8px; }
  .mark-gauge { display: flex; align-items: center; gap: 3px; font-weight: 800; font-size: 10px; line-height: 0.9; }
  .mark-gauge span small { display: block; font-size: 5px; }
  .mark-gauge i { width: 2px; height: 36px; background: var(--ink); }

  .headline {
    position: absolute; left: 540px; top: 92px; width: 420px; text-align: center;
    font-family: "Raleway", sans-serif; color: var(--ink); font-size: 24px; line-height: 1.08;
  }
  .headline strong { display: block; font-weight: 700; }
  .headline span { display: block; font-weight: 300; }
</style>
</head>
<body>
<div class="canvas">
  <section class="banner">
    <div class="banner-photo" role="img" aria-label="Outdoor kitchen island with stone countertop, shingle siding and two stainless steel double access doors beside a stainless refrigerator"></div>

    <div class="brand">
      <div class="brand-name">CRESTLINE</div>
      <div class="brand-tagline">outdoor kitchens</div>
    </div>

    <div class="benefits">
      <div class="benefit">
        <div class="benefit-mark">
          <svg width="46" height="46" viewBox="0 0 46 46" aria-hidden="true"><circle cx="23" cy="23" r="21" fill="var(--ink)"/></svg>
        </div>
        <div class="benefit-label">QUALITY</div>
        <div class="benefit-text">Our employees take Pride in their Work</div>
      </div>
      <div class="benefit">
        <div class="benefit-mark"><div class="mark-double">DOUBLE<br>WALL<small>CONSTRUCTION</small></div></div>
        <div class="benefit-label">VALUE</div>
        <div class="benefit-text">Our doors weigh 10 Pounds More than the competition</div>
      </div>
      <div class="benefit">
        <div class="benefit-mark"><div class="mark-grade">PREMIUM GRADE<b>304</b>STAINLESS STEEL</div></div>
        <div class="benefit-label">STRENGTH</div>
        <div class="benefit-text">Offers higher level of Corrosion Resistance</div>
      </div>
      <div class="benefit">
        <div class="benefit-mark"><div class="mark-gauge"><span>16G<small>FRAME</small></span><i></i><span>18G<small>OUTER WALL</small></span></div></div>
        <div class="benefit-label">DURABILITY</div>
        <div class="benefit-text">Thick and Durable Stainless Steel Construction</div>
      </div>
      <div class="benefit">
        <div class="benefit-mark">
          <svg width="46" height="46" viewBox="0 0 46 46" aria-hidden="true"><circle cx="23" cy="23" r="21" fill="var(--ink)"/></svg>
        </div>
        <div class="benefit-label">PEACE<br>OF MIND</div>
        <div class="benefit-text">Your Satisfaction is our highest priority</div>
      </div>
    </div>

    <h1 class="headline"><strong>OUTDOOR KITCHEN AND</strong><span>BBQ ISLAND ACCESSORIES</span></h1>
  </section>
</div>
</body>
</html>
```